Velmont Systems Business Card

Utilize the newly designed logo to create a polished, professional 2-sided business card for this IT Services company.

Target Market(s)

IT Professionals many in the telecommunications and medical industries.

Industry/Entity Type

Business

Requirements
Must have
• Use of new logo, identified color palette and font: Albertus MT Std Regular.

```html
<!DOCTYPE html>
<html lang="en">
<head>
<meta charset="utf-8">
<title>Velmont Systems — Business Card</title>
<link rel="stylesheet" href="https://fonts.googleapis.com/css2?family=Marcellus&display=swap">
<style>
  :root {
    --ink: #111111;
    --paper: #ffffff;
    --frame-light: #4a86c8;
    --frame-dark: #26308a;
    --rule: #3fb6e6;
    --brand: #1f3f8f;
    --brand-mark: #2f62b0;
  }
  html, body {
    margin: 0;
    padding: 0;
    width: 1200px;
    height: 685px;
    overflow: hidden;
    background: var(--paper);
  }
  .card {
    position: relative;
    width: 1200px;
    height: 685px;
    background: var(--paper);
    font-family: "Marcellus", "Times New Roman", serif;
    color: var(--ink);
  }
  .card-frame {
    position: absolute;
    inset: 0;
  }
  .holder-name,
  .holder-title,
  .contact-text,
  .brand-name,
  .brand-sub {
    position: absolute;
    margin: 0;
    line-height: 1;
    white-space: nowrap;
    font-weight: 400;
  }
  .holder-name {
    left: 58px;
    top: 60px;
    font-size: 80px;
    letter-spacing: 1px;
    word-spacing: 14px;
  }
  .holder-title {
    left: 61px;
    top: 139px;
    font-size: 44px;
  }
  .divider {
    position: absolute;
    left: 61px;
    top: 195px;
    width: 895px;
    height: 2px;
    background: var(--rule);
  }
  .contact-icon {
    position: absolute;
    left: 58px;
    width: 56px;
    height: 56px;
  }
  .contact-icon.phone { top: 239px; }
  .contact-icon.mail { top: 320px; }
  .contact-icon.web { top: 409px; }
  .contact-text {
    left: 144px;
    font-size: 39px;
  }
  .contact-text.phone { top: 246px; letter-spacing: 3px; }
  .contact-text.mail { top: 328px; }
  .contact-text.web { top: 416px; }
  .brand-mark {
    position: absolute;
    left: 690px;
    top: 504px;
    width: 142px;
    height: 142px;
    border-radius: 50%;
    background: var(--brand-mark);
  }
  .brand-name,
  .brand-sub {
    color: var(--brand);
  }
  .brand-name {
    left: 860px;
    top: 536px;
    font-size: 58px;
  }
  .brand-sub {
    left: 872px;
    top: 610px;
    font-size: 33px;
    letter-spacing: 3px;
  }
</style>
</head>
<body>
  <main class="card">
    <svg class="card-frame" width="1200" height="685" viewBox="0 0 1200 685" aria-hidden="true">
      <rect x="2" y="3" width="1185" height="666" fill="none" stroke="var(--frame-light)" stroke-width="4"/>
      <rect x="13" y="15" width="1185" height="667" fill="none" stroke="var(--frame-dark)" stroke-width="4"/>
    </svg>

    <h1 class="holder-name">FIRST LASTNAME</h1>
    <p class="holder-title">TITLE</p>
    <div class="divider"></div>

    <svg class="contact-icon phone" viewBox="0 0 56 56" aria-hidden="true">
      <circle cx="28" cy="28" r="23" fill="none" stroke="var(--ink)" stroke-width="3"/>
      <path d="M20 16 l5 -2 l4 8 l-4 3 q2 6 8 10 l3 -4 l8 4 l-2 5 q-4 3 -10 -1 q-10 -7 -13 -15 q-2 -5 1 -8z" fill="var(--ink)"/>
    </svg>
    <p class="contact-text phone">###-###-####</p>

    <svg class="contact-icon mail" viewBox="0 0 56 56" aria-hidden="true">
      <rect x="3" y="12" width="48" height="34" fill="none" stroke="var(--ink)" stroke-width="2"/>
      <path d="M3 12 L27 32 L51 12" fill="none" stroke="var(--ink)" stroke-width="2"/>
    </svg>
    <p class="contact-text mail">email@VS.com</p>

    <svg class="contact-icon web" viewBox="0 0 56 56" aria-hidden="true">
      <g fill="none" stroke="var(--ink)" stroke-width="1.6">
        <circle cx="28" cy="28" r="24"/>
        <ellipse cx="28" cy="28" rx="11" ry="24"/>
        <line x1="28" y1="4" x2="28" y2="52"/>
        <line x1="4" y1="28" x2="52" y2="28"/>
        <path d="M8 16 Q28 22 48 16"/>
        <path d="M8 40 Q28 34 48 40"/>
      </g>
    </svg>
    <p class="contact-text web">www.velmontsystems.com</p>

    <div class="brand-mark" aria-hidden="true"></div>
    <p class="brand-name">VELMONT</p>
    <p class="brand-sub">SYSTEMS</p>
  </main>
</body>
</html>
```